Health care center needs brochure design

We need a set of brochure designs for the 4 sections of our clinic, color coded based on the brand guidelines and with introduced icons to every section. The three sections include Biological Medicine (main medication tool is the IV tool), The Brindle Path program (main medication tool are the detox tools) , the Aesthetics section ( main medication tool is the syringe) and the lab (main tool is the microscope). You can find out more about our sections in the website www.velnortaclinic-example.com. The use of elements of the brand itself such as the lotus is also applicable.

Industry/Entity Type

Health Care

Requirements
Must have
• use of brand identity colors and features
• reflective medical icons
• color coding for each of the 4 sections based on the brand colors
Should not have
• pictures overused by other health care providers

```html
<!DOCTYPE html>
<html lang="en">
<head>
<meta charset="utf-8">
<title>Velnorta Integrated Care Center – Flyer</title>
<link href="https://fonts.googleapis.com/css2?family=Open+Sans:wght@400;600;700&display=swap" rel="stylesheet">
<style>
  :root {
    --mint: #82c9a9;
    --blush: #e4b9b1;
    --blush-text: #e2a89d;
    --ink: #4a4a4a;
    --white: #ffffff;
    --backdrop: #8a8a8a;
    --section-bio: #6fbf9b;
    --section-detox: #f2a57a;
    --section-aesthetics: #dc9e92;
    --section-lab: #86adc0;
  }
  * { margin: 0; padding: 0; box-sizing: border-box; }
  html, body { width: 948px; height: 1200px; overflow: hidden; }
  body { background: var(--backdrop); font-family: "Open Sans", sans-serif; }

  .flyer {
    position: absolute; left: 74px; top: 34px;
    width: 800px; height: 1132px;
    background: var(--white);
    display: flex; flex-direction: column;
  }

  .masthead { height: 171px; position: relative; flex: none; }
  .brand {
    position: absolute; left: 47px; top: 36px;
    display: flex; align-items: center; gap: 16px;
  }
  .brand-mark { width: 100px; height: 100px; border-radius: 50%; background: var(--mint); flex: none; }
  .brand-name {
    color: var(--mint); font-weight: 600; font-size: 17px; line-height: 21px;
    text-transform: uppercase; letter-spacing: 0.5px;
  }
  .booking {
    position: absolute; right: 98px; top: 56px; text-align: center;
    font-weight: 700; letter-spacing: 1px;
  }
  .booking-label { color: var(--mint); font-size: 17px; line-height: 21px; }
  .booking-phone { color: var(--blush-text); font-size: 17px; margin-top: 6px; letter-spacing: 0.5px; }

  .hero { height: 345px; position: relative; overflow: hidden; flex: none; }
  .hero-photo {
    position: absolute; inset: 0;
    background: linear-gradient(100deg, #dfe8ec 0%, #cbdbe2 40%, #e9eef0 62%, #b9cdd6 80%, #eef2f3 100%);
  }
  .hero-banner {
    position: absolute; left: 0; top: 112px; width: 406px; height: 140px;
    background: var(--blush);
    clip-path: polygon(0 0, 100% 0, 84.7% 100%, 0 100%);
    color: var(--white); text-align: center; padding: 28px 60px 0 20px;
  }
  .hero-kicker { font-size: 15px; font-weight: 600; letter-spacing: 0.8px; }
  .hero-title { font-size: 29px; font-weight: 700; line-height: 34px; letter-spacing: 1.5px; margin-top: 6px; }

  .welcome {
    height: 72px; flex: none; background: var(--mint); color: var(--white);
    display: flex; align-items: center; justify-content: center;
    font-size: 17px; font-weight: 700; letter-spacing: 0.6px;
  }

  .services {
    flex: 1; display: flex; justify-content: center; gap: 22px;
    padding-top: 26px;
  }
  .service { width: 160px; text-align: center; }
  .service-icon {
    width: 40px; height: 40px; border-radius: 50%;
    display: block; margin: 0 auto 8px;
  }
  .service-title {
    font-size: 17px; font-weight: 700; line-height: 21px;
    height: 46px; letter-spacing: 0.3px;
  }
  .service-text { color: var(--ink); font-size: 12.5px; line-height: 15.6px; margin-top: 4px; }
  .service--bio .service-title { color: var(--section-bio); }
  .service--bio .service-icon { background: var(--section-bio); }
  .service--detox .service-title { color: var(--section-detox); }
  .service--detox .service-icon { background: var(--section-detox); }
  .service--aesthetics .service-title { color: var(--section-aesthetics); }
  .service--aesthetics .service-icon { background: var(--section-aesthetics); }
  .service--lab .service-title { color: var(--section-lab); }
  .service--lab .service-icon { background: var(--section-lab); }

  .about {
    height: 159px; flex: none; background: var(--mint); color: var(--white);
    text-align: center; padding: 26px 74px 0;
  }
  .about-title { font-size: 18px; font-weight: 700; letter-spacing: 0.5px; }
  .about-text { font-size: 13px; line-height: 16.2px; margin-top: 12px; font-weight: 600; }

  .contact {
    height: 104px; flex: none; background: var(--blush); color: var(--white);
    display: flex; align-items: center; padding-left: 47px;
    font-size: 13px; line-height: 16.5px;
  }
  .contact-mark { width: 46px; height: 46px; border-radius: 50%; background: var(--mint); margin-right: 14px; flex: none; }
  .contact-address { width: 380px; font-style: normal; white-space: nowrap; flex: none; }
  .contact-divider { width: 1px; height: 62px; background: var(--white); margin-right: 13px; flex: none; }
  .contact-hours { white-space: nowrap; }
</style>
</head>
<body>
  <main class="flyer">
    <header class="masthead">
      <div class="brand">
        <span class="brand-mark"></span>
        <div class="brand-name">Velnorta<br>Integrated<br>Care Center</div>
      </div>
      <div class="booking">
        <div class="booking-label">SCHEDULE AN<br>APPOINTMENT</div>
        <div class="booking-phone">+971 2 555 0142</div>
      </div>
    </header>

    <section class="hero">
      <div class="hero-photo" role="img" aria-label="Photo of a smiling female doctor in a light blue headscarf and white coat, with colleagues in a bright medical center lobby behind her"></div>
      <div class="hero-banner">
        <p class="hero-kicker">The only regional clinic to offer</p>
        <h1 class="hero-title">SWISS BIOLOGICAL<br>MEDICINE</h1>
      </div>
    </section>

    <div class="welcome">Welcome to The First and Only Integrative Center of its kind in the Region</div>

    <section class="services">
      <article class="service service--bio">
        <svg class="service-icon" viewBox="0 0 40 40" aria-label="IV drip icon" role="img">
          <g fill="none" stroke="#fff" stroke-width="2" stroke-linecap="round" stroke-linejoin="round">
            <rect x="14" y="8" width="12" height="15" rx="3"/>
            <line x1="17" y1="14" x2="23" y2="14"/>
            <path d="M20 23v4c0 3 -4 3 -4 6"/>
          </g>
        </svg>
        <h2 class="service-title">Swiss Biological<br>Medicine</h2>
        <p class="service-text">An alternative health care approach that aims to identify the root cause of your illness. Using multiple diagnostic procedures and supporting conventional methods to restore the bodies equilibrium.</p>
      </article>
      <article class="service service--detox">
        <svg class="service-icon" viewBox="0 0 40 40" aria-label="Detox bottle icon" role="img">
          <g fill="none" stroke="#fff" stroke-width="2" stroke-linecap="round" stroke-linejoin="round">
            <path d="M17 9h6M18 9v5l-4 4v13h12V18l-4-4V9"/>
            <path d="M17 25c2-4 5-4 6-4c0 3-2 6-6 4z"/>
          </g>
        </svg>
        <h2 class="service-title">Brindle Path<br>Program</h2>
        <p class="service-text">A total mind-body healing program that combines both Eastern healing arts and Western modern medicine to guide you towards better physical health and emotional well being in a complete life transformimg experience.</p>
      </article>
      <article class="service service--aesthetics">
        <svg class="service-icon" viewBox="0 0 40 40" aria-label="Syringe icon" role="img">
          <g fill="none" stroke="#fff" stroke-width="2" stroke-linecap="round" stroke-linejoin="round">
            <rect x="15" y="12" width="8" height="16" rx="1" transform="rotate(45 19 20)"/>
            <line x1="25" y1="14" x2="29" y2="10"/>
            <line x1="27" y1="8" x2="31" y2="12"/>
            <line x1="13" y1="26" x2="9" y2="30"/>
          </g>
        </svg>
        <h2 class="service-title">Aesthetics</h2>
        <p class="service-text">To complete your rejuvenation inside out the center offers the latest technologies for skin care and total body treatments that nourishs and restores it.</p>
      </article>
      <article class="service service--lab">
        <svg class="service-icon" viewBox="0 0 40 40" aria-label="Microscope icon" role="img">
          <g fill="none" stroke="#fff" stroke-width="2" stroke-linecap="round" stroke-linejoin="round">
            <rect x="17" y="8" width="5" height="12" rx="1" transform="rotate(-25 19.5 14)"/>
            <path d="M24 20a6 6 0 0 1 -4 10"/>
            <line x1="12" y1="31" x2="28" y2="31"/>
            <line x1="15" y1="24" x2="22" y2="24"/>
          </g>
        </svg>
        <h2 class="service-title">Laboratory</h2>
        <p class="service-text">Our in-house lab provides precise diagnostics and detailed analyses that guide every treatment plan and follow your progress along the way.</p>
      </article>
    </section>

    <section class="about">
      <h2 class="about-title">ABOUT THE CENTER</h2>
      <p class="about-text">We are proud to be the first to provide alternative biologocal medicine in the region integrated with programs that envelope the healing process in a complete cycle touching The Body, The Mind and The Soul. The Center provides access to new ways of healing via Ayurverdic medicine and Aesthetic procedures. It also provides new diagnostics and regime treatments to encompass the needs of your body taking it towards its natural healthy state in a happy purified mind and soul.</p>
    </section>

    <footer class="contact">
      <span class="contact-mark"></span>
      <address class="contact-address">Velnorta Integrated Care Center<br>PO Box 40210, Abu Dhabi, Al Reem, Marina East<br>United Arab Emirates, 02-555 0142, info@velnortacc.com</address>
      <span class="contact-divider"></span>
      <p class="contact-hours">Opening hours: Sat- Thurs: 11am - 7pm<br>Ramadan Timing: SAT- WED:&nbsp; 6 pm - 12 am</p>
    </footer>
  </main>
</body>
</html>
```